My Professional Resume/CV Design

Hi Pixel Harbor experts, I need a professional resume/CV design for using my carrier hiring activities. I have a draft and this draft is 2 types.
1) Traditional IT Major Company Senior(Manager Level) to Director level application (File: Tanabe_Mirei_Res_EN2023AprA)
>Application example companies: Velmora, Drant, Quenta, Tidewicket, VossLattice, Brisk Vale, Hexaplume, Korvani, Zuvetra, Ferno, uMox, Wirlpeak etc
>This should not be fancy. Please make format with traditional/gentle/standard but also need to appear unique point such as icons, borderlines etc
2) Cutting-Edge (Web 3.0/metaverse/NFT/Crypto) Start-up or Young (Less 5 year's history) Company Director and C-Levels position application (Tanabe_Mirei_Res_EN2023Apr_typeC)
>Application Example Companies: Perilux Studios, Quorvex, Nexlorry.net, Dovecrest, FarDune, KelpVaultix, Ravello, Zipo/Tolk/Verm, Plunket, VESKARD, quillNRX etc
>This resume format should be something "edge" "advanced" "future" and "high-tech", so need to your high sense of design technics.
Both drafts is without a profile picture, but I need to put in my portfolio picture (Just attached one is my 2018's, you can trim and edit as well)
For the document format, please send me to WORD and PAGES both. and total MAX 2 page in all contents please (No more 3 pages)
Target Market(s)
Traditional Major Tech Company's VP/Directors or/and Latest Web 3.0 StartUp C-Levels (CEO/CTO/CSO/COO etc)
Industry/Entity Type
Technology
Font styles to use
Other font styles liked:
- Choose 3 a)Century Gothic b) Avenir c)Graphik d)Kohinoor e)Optima f)Platino
Look and feel
Each slider illustrates characteristics of the customer's brand and the style your logo design should communicate.

```html
<!DOCTYPE html>
<html lang="en">
<head>
<meta charset="utf-8">
<title>Resume – Page 2</title>
<link href="https://fonts.googleapis.com/css2?family=Arimo:wght@400&display=swap" rel="stylesheet">
<style>
  :root {
    --accent: #9c4b9c;
    --body: #7a7a7a;
    --ink: #111111;
    --dot-dark: #555555;
    --paper: #ffffff;
  }
  * { box-sizing: border-box; margin: 0; padding: 0; }
  html, body { width: 882px; height: 1200px; overflow: hidden; background: var(--paper); }
  .page {
    width: 882px; height: 1200px;
    padding: 26px 100px 0 75px;
    font-family: "Arimo", Arial, sans-serif;
    font-size: 13.3px;
    color: var(--body);
  }
  .achievements { list-style: none; }
  .achievements li {
    position: relative;
    padding-left: 27px;
    line-height: 17.6px;
    margin-bottom: 3px;
  }
  .achievements li::before {
    content: "";
    position: absolute; left: 4px; top: 7px;
    width: 4px; height: 4px; border-radius: 50%;
    background: #9a9a9a;
  }
  .role { margin-top: 32px; }
  .company, .period, .section-title {
    color: var(--accent); line-height: 18.5px; font-size: 13.8px;
  }
  .position { color: var(--ink); line-height: 18.5px; font-size: 13.8px; }
  .label { color: var(--ink); font-size: 12.4px; margin-top: 19px; margin-bottom: 3px; line-height: 16px; }
  .section-title { margin-top: 29px; }
  .title-dots { display: block; margin-top: 6px; }
  .degree { color: var(--ink); font-size: 13.8px; line-height: 18.5px; margin-top: 3px; }
  .school { font-size: 13.8px; line-height: 18.5px; }
</style>
</head>
<body>
<main class="page">
  <ul class="achievements">
    <li>Created program/production budgets and completed all interactions with the research institute on behalf of the TV station.</li>
    <li>Planned the 12 episodes of the first episode of the new TV program.</li>
    <li>Spearheaded Japan and China's incorporation in the investigation and introduction of cutting-edge technology to enhance operational productivity and efficiency for Bahrain partners.</li>
    <li>Presented Humanoid robotics usage for TV presenter collaborated with Manama Vision TV directors in the Ministry of Digital Services.</li>
    <li>Successfully navigated and managed the challenges posed by the funding freeze for six months due to the pandemic.</li>
  </ul>

  <section class="role">
    <p class="company">Corvane Tech Limited (Strandmoor Group (Holdings) Ltd., Hong Kong</p>
    <p class="period">May 2016 – March 2019</p>
    <p class="position">Head of Division</p>
    <p class="label">Key Achievements:</p>
    <ul class="achievements">
      <li>Started work as one of the key players of the Fin-Tech industry, management, and head of operations of a platform for digital assets.</li>
      <li>Outperformed corporate expectations in leading and supervising digital asset white label exchange operations by improving systems that could not be managed before joining and implementing process improvement initiatives and manuals.</li>
      <li>Adept in managing multiple projects, achieving stable operational exchange, contributing to end-user increase from 1.5K to 5K.</li>
      <li>Achieved four promotions in two years, resulting in career breakthroughs.</li>
      <li>Nominated Taiwan subsidiary head of a startup, spearheaded global business operations while overseeing the Taiwan subsidiary business expansion to Taiwanese partner b2b clients and handover to the local manager between May to Oct 2017.</li>
      <li>Pioneered a customized Digital Asset Exchange platform, process improvement initiatives, facilitating prompt delivery to clients.</li>
      <li>Delivered digital assets to clients using exceptional customer service management to generate business while facilitating customers' integration wallet and listing exchange for each industry’s digital asset. Total fund-raising amount was over US$ 1B.</li>
      <li>Displayed solid leadership abilities in team-building/mentoring activities and optimized project branding processes involving HR oversight and staffing as well as financial control for each project.</li>
    </ul>
  </section>

  <section class="role">
    <p class="company">PT. Selvara Bali, Tokyo &amp; Denpasar</p>
    <p class="period">2014 – 2015</p>
    <p class="position">Project Manager</p>
    <p class="label">Key Achievements:</p>
    <ul class="achievements">
      <li>Received a stellar review for strategic planning of corporate projects with B2B institutions at Bali of Indonesia Microfinance and Property Corporate.</li>
      <li>Successfully relocated to Hong Kong in late 2015 for personal reasons.</li>
    </ul>
  </section>

  <section class="role">
    <p class="company">Meridal Agency, Tokyo</p>
    <p class="period">2010 – 2014</p>
    <p class="position">Chief Operations Officer</p>
    <p class="label">Key Achievements:</p>
    <ul class="achievements">
      <li>Structured and pioneered the process of running the Tokyo branch of a Singaporean restaurant, effectively connecting with the F&amp;B company to ensure success.</li>
      <li>Demonstrated strength in PR, including the English Media, to increase brand awareness and drive clientele growth.</li>
      <li>Successfully met the business cessation requirements of the JV Agreement.</li>
    </ul>
  </section>

  <section>
    <h2 class="section-title" style="font-weight:400">QUALIFICATIONS:</h2>
    <svg class="title-dots" width="24" height="12" viewBox="0 0 24 12" aria-hidden="true">
      <circle cx="6" cy="6" r="5.5" fill="var(--dot-dark)"/>
      <circle cx="17" cy="6" r="5.5" fill="var(--accent)"/>
    </svg>
    <p class="degree">Bachelor’s Degree in Economics/Philosphy</p>
    <p class="school">University of Kaseno, Japan</p>
  </section>
</main>
</body>
</html>
```